Healthcare marketing Website design

This is for a healthcare marketing agency
All details and brief included in the files

I need the design to be incredible!

5 pages to be designed
Home page
About
Portfolio Page
Services
Start your project page

If you need more stock images - download preview images from kelmora pix so I can purchase at a later date

```html
<!DOCTYPE html>
<html lang="en">
<head>
<meta charset="utf-8">
<title>Quillmere Consulting – Healthcare Marketing</title>
<link href="https://fonts.googleapis.com/css2?family=Comfortaa:wght@400;600;700&display=swap" rel="stylesheet">
<style>
:root{
  --navy:#1f2b4d;
  --blue:#1b8fd6;
  --sky:#29b6f0;
  --sky-pale:#e3f5fd;
  --ink:#2b2f3a;
  --muted:#6b7180;
  --grey-bg:#eeeff1;
  --line:#d9dce2;
  --footer:#1d2029;
  --footer-deep:#15171e;
  --white:#ffffff;
}
*{box-sizing:border-box;margin:0;padding:0}
html,body{width:1200px;height:4948px;overflow:hidden}
body{font-family:"Comfortaa",sans-serif;color:var(--ink);background:var(--white);position:relative}
.section{position:absolute;left:0;width:1200px}
.btn{display:inline-block;height:46px;line-height:46px;padding:0 30px;font-size:13px;font-weight:700;letter-spacing:.5px;border-radius:3px;color:var(--white);text-decoration:none;white-space:nowrap}
.btn--navy{background:var(--navy)}
.btn--sky{background:var(--sky)}
.btn-row{display:flex;gap:22px;justify-content:center}

/* header */
.brand{display:flex;align-items:center;gap:10px;font-weight:700;font-size:26px;color:var(--white);white-space:nowrap}
.brand__dot{width:22px;height:22px;border-radius:50%;background:var(--sky)}
.site-header{position:absolute;top:26px;left:90px;right:70px;height:60px;display:flex;align-items:center;z-index:3}
.main-nav{margin-left:auto;display:flex;gap:28px;align-items:center;font-size:14px;color:var(--navy);font-weight:600;white-space:nowrap}
.main-nav .is-active{color:var(--sky)}
.social-row{position:absolute;top:92px;left:790px;display:flex;gap:18px;z-index:3}
.social-dot{width:34px;height:34px;border-radius:50%;background:var(--navy)}

/* hero */
.hero{top:0;height:780px}
.hero__wave{position:absolute;top:0;left:0}
.hero__art{position:absolute;left:690px;top:150px;width:450px;height:560px;border-radius:40px;background:radial-gradient(circle at 55% 45%,#cfefff 0%,#8fd6f7 45%,#e9f7fe 80%,rgba(255,255,255,0) 100%)}
.hero__copy{position:absolute;left:100px;top:225px;width:560px;color:var(--white)}
.hero__title{font-size:42px;line-height:1.22;font-weight:700}
.hero__lead{margin-top:40px;font-size:22px;line-height:1.35;font-weight:600}
.hero__stat{margin-top:28px;font-size:17px;font-weight:700}
.hero__copy .btn-row{justify-content:flex-start;margin-top:46px}

/* intro */
.intro{top:790px;height:600px;text-align:center}
.intro .brand{justify-content:center;color:var(--navy);font-size:30px;margin-top:30px}
.intro__title{margin-top:34px;font-size:30px;font-weight:600;color:var(--ink)}
.intro__text{width:640px;margin:24px auto 0;font-size:13.5px;line-height:1.7;color:var(--muted)}
.intro__text + .intro__text{margin-top:22px}
.intro .btn-row{margin-top:44px}
.divider{position:absolute;top:1400px;left:0;width:1200px;height:2px;background:var(--line)}

/* stats */
.stats{top:1420px;height:800px}
.stats__art{position:absolute;left:770px;top:10px;width:370px;height:240px;background:linear-gradient(160deg,#eef2f8,#dfe6f0)}
.stats__title{position:absolute;left:100px;top:30px;font-size:30px;font-weight:600}
.stats__text{position:absolute;left:100px;width:640px;font-size:13.5px;line-height:1.6;color:var(--ink)}
.ring{position:absolute;top:250px;width:300px;text-align:center}
.ring svg{display:block;margin:0 auto}
.ring__label{margin-top:30px;font-size:19px;font-weight:600;white-space:nowrap}
.stats .btn-row{position:absolute;left:0;right:0;top:640px}

/* testimonials */
.reviews{top:2230px;height:760px}
.reviews__title{text-align:center;font-size:38px;font-weight:600;color:var(--sky);margin-top:60px}
.reviews__band{position:absolute;top:150px;left:0;width:1200px;height:420px;background:var(--sky-pale)}
.review-card{position:absolute;top:158px;left:100px;width:990px;height:404px;background:var(--white);border:6px solid #9edcf6}
.review-card__photo{position:absolute;left:18px;top:14px;width:364px;height:364px;background:linear-gradient(180deg,#f0f0f0 0%,#c9ccd1 60%,#2c3140 100%)}
.review-card__body{position:absolute;left:440px;top:30px;width:500px}
.review-card__name{font-size:20px;font-weight:700}
.review-card__company{font-size:14px;color:var(--muted);margin-top:4px}
.review-card__quote{margin-top:28px;font-size:16px;line-height:1.45;color:var(--ink)}
.arrow{position:absolute;top:340px}
.reviews .btn-row{position:absolute;left:0;right:0;top:630px}

/* faq */
.faq{top:3010px;height:660px;background:var(--grey-bg)}
.faq__title{text-align:center;font-size:40px;font-weight:400;margin-top:70px;color:var(--ink);letter-spacing:1px}
.faq__figure{position:absolute;left:760px;top:180px;width:300px;height:480px;border-radius:150px 150px 0 0;background:linear-gradient(180deg,#a5a7ab,#7d8085)}
.faq-list{position:absolute;left:110px;top:185px;width:500px;list-style:none}
.faq-item{background:var(--white);border:1px solid var(--line);margin-bottom:12px;font-size:12.5px}
.faq-item__q{display:flex;align-items:center;justify-content:space-between;height:46px;padding:0 16px;color:var(--navy)}
.faq-item__icon{width:24px;height:24px;border-radius:50%;border:1px solid var(--line);display:flex;align-items:center;justify-content:center;font-size:15px;color:var(--sky)}
.faq-item--open .faq-item__q{background:var(--sky);color:var(--white)}
.faq-item--open .faq-item__icon{background:var(--white);border:none}
.faq-item__a{padding:18px 16px 22px;line-height:1.7;color:var(--muted)}

/* blog */
.blog{top:3670px;height:770px}
.blog__title{text-align:center;font-size:40px;font-weight:400;margin-top:70px;letter-spacing:1px}
.post{position:absolute;top:185px;width:320px}
.post__image{height:200px}
.post__body{margin:-30px 18px 0;position:relative;background:var(--white);box-shadow:0 6px 20px rgba(0,0,0,.12);padding:22px 22px 26px}
.post__meta{font-size:11px;color:var(--muted);display:flex;gap:18px}
.post__title{margin-top:12px;font-size:17px;font-weight:700;color:var(--blue)}
.post__text{margin-top:14px;font-size:13px;line-height:1.6;color:var(--muted)}
.post__more{margin-top:18px;font-size:13px;font-weight:700}

/* footer */
.site-footer{top:4440px;height:420px;background:var(--footer);color:#c9ccd4}
.footer-col{position:absolute;top:80px}
.footer-col__title{font-size:16px;font-weight:700;color:var(--white);letter-spacing:.5px}
.site-footer .brand{font-size:26px}
.footer-about{margin-top:30px;width:250px;font-size:12px;line-height:1.7}
.contact-line{display:flex;gap:12px;align-items:center;margin-top:16px;font-size:12px;white-space:nowrap}
.link-list{list-style:none;margin-top:34px;font-size:13px}
.link-list li{margin-bottom:14px}
.link-list li::before{content:"›";color:var(--sky);margin-right:10px}
.gallery{margin-top:34px;display:grid;grid-template-columns:repeat(3,60px);gap:8px}
.gallery span{height:60px;background:var(--white)}
.gallery .is-dark{background:#2f3340}
.subscribe-label{margin-top:34px;font-size:12px}
.subscribe-field{margin-top:14px;width:250px;height:40px;background:#2a2e3a;display:flex;align-items:center;justify-content:space-between;padding:0 12px;font-size:12px;color:#8b90a0}
.subscribe-field b{width:22px;height:22px;background:var(--sky);border-radius:2px}
.footer-social{display:flex;gap:14px;margin-top:24px}
.footer-social span{width:34px;height:34px;border-radius:50%;background:#3a3f4d}
.footer-social .is-sky{background:var(--sky)}
.bottom-bar{top:4860px;height:88px;background:var(--footer-deep);text-align:center;line-height:88px;font-size:12px;color:#b0b4c0}
</style>
</head>
<body>

<header class="site-header">
  <div class="brand"><span class="brand__dot"></span>Quillmere</div>
  <nav class="main-nav">
    <span class="is-active">Home</span><span>About</span><span>Portfolio</span><span>Contact Us</span><span>Our Services</span><span>Blog</span>
    <a class="btn btn--navy" style="height:38px;line-height:38px;padding:0 20px">Start Your Project</a>
  </nav>
</header>
<div class="social-row"><span class="social-dot"></span><span class="social-dot"></span><span class="social-dot"></span><span class="social-dot"></span><span class="social-dot"></span><span class="social-dot"></span></div>

<section class="section hero">
  <svg class="hero__wave" width="1200" height="780" viewBox="0 0 1200 780" aria-hidden="true">
    <defs><linearGradient id="heroBlue" x1="0" y1="0" x2="1" y2="1"><stop offset="0" stop-color="#1b6fc2"/><stop offset="1" stop-color="#1f2b6d"/></linearGradient></defs>
    <path d="M0 0H560C520 120 640 190 720 260C820 350 760 500 640 560C520 620 380 590 250 660C170 705 90 760 0 760Z" fill="url(#heroBlue)"/>
    <path d="M0 760C120 700 220 640 360 625C470 612 560 650 660 610" fill="none" stroke="#29b6f0" stroke-width="4"/>
  </svg>
  <div class="hero__art" role="img" aria-label="Illustration of a hand holding a smartphone showing a doctor profile app"></div>
  <div class="hero__copy">
    <h1 class="hero__title">Don't miss a new opportunity to grow you practice with your online presence.</h1>
    <p class="hero__lead">Being online a large opportunity for your practice</p>
    <p class="hero__stat">80% of internet uses search for health information</p>
    <div class="btn-row"><a class="btn btn--sky">CONTACT US</a><a class="btn btn--navy">START YOUR PROJECT</a></div>
  </div>
</section>

<section class="section intro">
  <div class="brand"><span class="brand__dot"></span>Quillmere</div>
  <h2 class="intro__title">Helping Those Who Help Others</h2>
  <p class="intro__text">You became a health professional because you wanted to make a difference and you obviously care about patient outcomes. At first things went great and you had plenty of patients calling, but now a new practice has opened down the road, offering the same types of services and products at lower prices. Regular patients haven't come back to you in a while and you know you need to do something, but the old ways like relying on word of mouth no longer seem to be working and suddenly you don't know how to get started. That is exactly where we can help. Quillmere Consulting specializes in helping health professionals like you create a great online user experience for prospective patients.</p>
  <p class="intro__text">We help you build your online assets through Website Development, Social media marketing, Online Traffic Strategies.</p>
  <div class="btn-row"><a class="btn btn--navy">CONTACT US</a><a class="btn btn--sky">START YOUR PROJECT</a></div>
</section>

<div class="divider"></div>

<section class="section stats">
  <div class="stats__art" role="img" aria-label="Faint decorative illustration of a clinic building"></div>
  <h2 class="stats__title">Helping Clients Since 2015:</h2>
  <p class="stats__text" style="top:82px">Quillmere Consulting specializes in helping health professionals. We say stand out from the busy crowd, find new patients and keep you top of mind as the go-to person within your industry. Unlike most health professionals who solely rely on word of mouth, we use the latest online marketing techniques to grow you and your practice.</p>
  <p class="stats__text" style="top:172px">While our niche has always been in the healthcare industry, Quillmere Marketing also has experience in providing solutions our e-commerce partners as well as other professional industries.</p>

  <div class="ring" style="left:96px">
    <svg width="210" height="210" viewBox="0 0 210 210" aria-hidden="true">
      <circle cx="105" cy="105" r="95" fill="none" stroke="#cfd3da" stroke-width="3"/>
      <circle cx="105" cy="105" r="95" fill="none" stroke="#29b6f0" stroke-width="9" stroke-dasharray="376 597" transform="rotate(-90 105 105)"/>
      <text x="105" y="118" text-anchor="middle" font-family="Comfortaa, sans-serif" font-size="40" fill="#29b6f0">63%</text>
    </svg>
    <p class="ring__label">Healthcare and medical</p>
  </div>
  <div class="ring" style="left:475px">
    <svg width="210" height="210" viewBox="0 0 210 210" aria-hidden="true">
      <circle cx="105" cy="105" r="95" fill="none" stroke="#1f2b4d" stroke-width="9"/>
      <circle cx="105" cy="105" r="95" fill="none" stroke="#29b6f0" stroke-width="9" stroke-dasharray="149 597" transform="rotate(-90 105 105)"/>
      <text x="105" y="118" text-anchor="middle" font-family="Comfortaa, sans-serif" font-size="40" fill="#2b2f3a">25%</text>
    </svg>
    <p class="ring__label">Ecommerce Projects</p>
  </div>
  <div class="ring" style="left:803px">
    <svg width="210" height="210" viewBox="0 0 210 210" aria-hidden="true">
      <circle cx="105" cy="105" r="95" fill="none" stroke="#1f2b4d" stroke-width="9"/>
      <circle cx="105" cy="105" r="95" fill="none" stroke="#29b6f0" stroke-width="9" stroke-dasharray="72 597" transform="rotate(-90 105 105)"/>
      <text x="105" y="118" text-anchor="middle" font-family="Comfortaa, sans-serif" font-size="40" fill="#2b2f3a">12%</text>
    </svg>
    <p class="ring__label">Other Professional Services</p>
  </div>
  <div class="btn-row"><a class="btn btn--navy">CONTACT US</a><a class="btn btn--sky">START YOUR PROJECT</a></div>
</section>

<section class="section reviews">
  <h2 class="reviews__title">See what our clients say:</h2>
  <div class="reviews__band"></div>
  <svg class="arrow" style="left:44px" width="24" height="40" viewBox="0 0 24 40" aria-hidden="true"><path d="M20 4L6 20L20 36" fill="none" stroke="#1b8fd6" stroke-width="4"/></svg>
  <svg class="arrow" style="left:1134px" width="24" height="40" viewBox="0 0 24 40" aria-hidden="true"><path d="M4 4L18 20L4 36" fill="none" stroke="#1b8fd6" stroke-width="4"/></svg>
  <article class="review-card">
    <div class="review-card__photo" role="img" aria-label="Portrait photo of a client in a business suit"></div>
    <div class="review-card__body">
      <p class="review-card__name">Client 1</p>
      <p class="review-card__company">Company Name</p>
      <p class="review-card__quote">Sed ut perspiciatis unde omnis iste natus error sit voluptatem accusantium doloremque laudantium, totam rem aperiam, eaque ipsa quae ab illo inventore.</p>
      <p class="review-card__quote" style="margin-top:20px">Sed ut perspiciatis unde omnis iste natus error sit voluptatem accusantium doloremque laudantium, totam rem aperiam, eaque ipsa quae ab illo inventore.</p>
    </div>
  </article>
  <div class="btn-row"><a class="btn btn--navy">CONTACT US</a><a class="btn btn--sky">START YOUR PROJECT</a></div>
</section>

<section class="section faq">
  <h2 class="faq__title">MOST COMMON QUESTIONS</h2>
  <ul class="faq-list">
    <li class="faq-item"><div class="faq-item__q">01. Who has access to my health records?<span class="faq-item__icon">+</span></div></li>
    <li class="faq-item faq-item--open"><div class="faq-item__q">02. What information can be found in my health record?<span class="faq-item__icon">−</span></div>
      <p class="faq-item__a">Your health record holds your visit notes, test results, current medicines and allergies. Only your care team can read it, and you may ask for a full copy at any time. We keep every record private, secure and up to date so each visit runs smoothly.</p></li>
    <li class="faq-item"><div class="faq-item__q">03. How often should my practice update its online profile?<span class="faq-item__icon">+</span></div></li>
    <li class="faq-item"><div class="faq-item__q">04. What information can be found in my health record?<span class="faq-item__icon">+</span></div></li>
    <li class="faq-item"><div class="faq-item__q">05. Who has access to my health records?<span class="faq-item__icon">+</span></div></li>
  </ul>
  <div class="faq__figure" role="img" aria-label="Grey silhouette of a person standing"></div>
</section>

<section class="section blog">
  <h2 class="blog__title">BLOG POSTS</h2>
  <article class="post" style="left:82px">
    <div class="post__image" role="img" aria-label="Photo of a doctor's desk with a stethoscope" style="background:linear-gradient(135deg,#c6a58f,#8d6b5c)"></div>
    <div class="post__body"><div class="post__meta"><span>Health</span><span>2 Comments</span></div><h3 class="post__title">Donec venenatis turpis</h3><p class="post__text">We can help your practice grow online with new patients and better care for everyone who visits you.</p><p class="post__more">Reading...</p></div>
  </article>
  <article class="post" style="left:440px">
    <div class="post__image" role="img" aria-label="Photo of a clinician reviewing a digital health screen" style="background:linear-gradient(135deg,#b7d7ec,#4d86b6)"></div>
    <div class="post__body"><div class="post__meta"><span>Health</span><span>2 Comments</span></div><h3 class="post__title">Donec venenatis turpis</h3><p class="post__text">We can help your practice grow online with new patients and better care for everyone who visits you.</p><p class="post__more">Reading...</p></div>
  </article>
  <article class="post" style="left:798px">
    <div class="post__image" role="img" aria-label="Photo of medical supplies on a bright table" style="background:linear-gradient(135deg,#e6e0dc,#b9928a)"></div>
    <div class="post__body"><div class="post__meta"><span>Health</span><span>2 Comments</span></div><h3 class="post__title">Donec venenatis turpis</h3><p class="post__text">We can help your practice grow online with new patients and better care for everyone who visits you.</p><p class="post__more">Reading...</p></div>
  </article>
</section>

<footer class="section site-footer">
  <div class="footer-col" style="left:100px">
    <div class="brand"><span class="brand__dot"></span>Quillmere</div>
    <p class="footer-about">All of our digital marketing comes from proven methods that have been tested and have worked across many industries.</p>
    <p class="contact-line"><svg width="14" height="14" viewBox="0 0 24 24" aria-hidden="true"><path d="M6 2l4 4-2 3c1 3 4 6 7 7l3-2 4 4-3 4C10 21 3 14 2 5z" fill="#29b6f0"/></svg>+1 555 014 2290</p>
    <p class="contact-line"><svg width="14" height="14" viewBox="0 0 24 24" aria-hidden="true"><rect x="2" y="5" width="20" height="14" fill="none" stroke="#29b6f0" stroke-width="2"/><path d="M2 5l10 8 10-8" fill="none" stroke="#29b6f0" stroke-width="2"/></svg>hello@quillmereconsulting.test</p>
    <p class="contact-line"><svg width="14" height="14" viewBox="0 0 24 24" aria-hidden="true"><path d="M12 2a7 7 0 0 0-7 7c0 5 7 13 7 13s7-8 7-13a7 7 0 0 0-7-7z" fill="#29b6f0"/><circle cx="12" cy="9" r="2.5" fill="#1d2029"/></svg>210 Harlow Lane, Fenwick, ST 4420</p>
  </div>
  <div class="footer-col" style="left:400px">
    <p class="footer-col__title">USEFULL LINKS</p>
    <ul class="link-list"><li>Home</li><li>About</li><li>Portfolio</li><li>Contact Us</li><li>Our Services</li><li>Blog</li></ul>
  </div>
  <div class="footer-col" style="left:610px">
    <p class="footer-col__title">SNAPLINE GALLERY</p>
    <div class="gallery"><span class="is-dark"></span><span></span><span class="is-dark"></span><span></span><span class="is-dark"></span><span></span><span class="is-dark"></span><span></span><span class="is-dark"></span></div>
  </div>
  <div class="footer-col" style="left:850px">
    <p class="footer-col__title">SUBSCRIBE</p>
    <p class="subscribe-label">Subscribe to the newsletter</p>
    <div class="subscribe-field">Your email here<b></b></div>
    <div class="footer-social"><span></span><span class="is-sky"></span><span></span><span></span><span></span></div>
  </div>
</footer>
<div class="section bottom-bar">©2022 Quillmere Consultancy | All rights reserved. Privacy Policy | Terms and conditions</div>

</body>
</html>
```